Fernvale Accounting - New Postcard for B2B marketing

I need a postcard for my business that provides cloud-based bookkeeping services with LedgerCloud Online. Our clients are small independently owned businesses. Please use our website for inspiration (colors, content, etc)... www.FernvaleAccounting.com.

Target Market(s)

Small, independently-owned businesses, including restaurants, retail stores, small medical practices, etc

Industry/Entity Type

Bookkeeper

Font styles to use
Serif

Colors
3276b5
155ea9
c4d6e9
85cae6
33a6d7

Requirements
Must have
• Must have my logo (see attached), business contact info (see website), description of services, blue color scheme
Nice to have
• Maybe add "Prices starting at $750/mo"
Content should match info on our website
4 x 6 horizontal postcard (see attached template)

```html
<!DOCTYPE html>
<html lang="en">
<head>
<meta charset="utf-8">
<title>Fernvale Accounting Postcard</title>
<link href="https://fonts.googleapis.com/css2?family=Libre+Baskerville:wght@400;700&display=swap" rel="stylesheet">
<style>
  :root {
    --blue-deep: #155ea9;
    --blue-mid: #3276b5;
    --blue-pale: #c4d6e9;
    --blue-sky: #85cae6;
    --ink-navy: #2b3990;
    --white: #ffffff;
    --rule: #8a8a8a;
    --serif: "Libre Baskerville", Georgia, serif;
  }
  * { box-sizing: border-box; margin: 0; padding: 0; }
  html, body { width: 1200px; height: 1200px; overflow: hidden; background: var(--white); }
  body { position: relative; font-family: var(--serif); color: var(--white); }

  .card { position: absolute; left: 235px; width: 784px; height: 530px; border: 1px solid var(--rule); overflow: hidden; background: var(--white); }
  .card--front { top: 47px; }
  .card--back { top: 619px; }

  /* Front */
  .brand { position: absolute; left: 26px; top: 70px; display: flex; align-items: center; gap: 8px; color: var(--blue-deep); font-size: 21px; font-weight: 400; }
  .brand__mark { width: 13px; height: 13px; background: var(--blue-deep); }

  .service-col { position: absolute; bottom: 0; width: 262px; background: linear-gradient(90deg, #1a5daa 0%, #2a78b8 100%); }
  .service-col--books { left: 0; top: 189px; }
  .service-col--reports { left: 261px; top: 109px; }
  .service-col--payroll { left: 522px; top: 0; }

  .services-title { position: absolute; top: 42px; left: 422px; font-size: 41px; letter-spacing: -0.5px; white-space: nowrap; line-height: 1; }
  .services-title .our { color: var(--blue-deep); }
  .services-title .rest { color: var(--white); margin-left: 8px; }

  .service { position: absolute; top: 196px; width: 262px; }
  .service--books { left: 0; }
  .service--reports { left: 261px; }
  .service--payroll { left: 522px; }
  .service__icon { display: block; margin: 0 auto; width: 84px; height: 84px; }
  .service__name { font-weight: 700; font-size: 16px; letter-spacing: 0.3px; text-align: center; margin-top: 12px; white-space: nowrap; }
  .service__text { font-size: 14.6px; line-height: 21.3px; margin-top: 14px; white-space: nowrap; }
  .service--books .service__text { padding-left: 18px; }
  .service--reports .service__text { padding-left: 8px; }
  .service--payroll .service__text { padding-left: 14px; }

  /* Back */
  .promo { position: absolute; left: 0; top: 0; width: 392px; height: 100%; background: linear-gradient(90deg, #2a78b8 0%, #1a5daa 100%); }
  .promo__lead { position: absolute; left: 24px; top: 22px; font-size: 20.5px; line-height: 32px; white-space: nowrap; }
  .price { position: absolute; left: 31px; top: 163px; width: 330px; height: 144px; border-radius: 50%; background: var(--blue-sky); color: var(--ink-navy); text-align: center; }
  .price__lead { font-size: 31px; margin-top: 26px; line-height: 1; }
  .price__amount { font-size: 42px; margin-top: 10px; line-height: 1; }
  .cta { position: absolute; left: 33px; top: 327px; display: flex; align-items: center; gap: 10px; font-size: 33px; line-height: 1; white-space: nowrap; }
  .cta__icon { width: 44px; height: 44px; }
  .contact { position: absolute; left: 19px; display: flex; align-items: center; gap: 12px; white-space: nowrap; }
  .contact__badge { width: 28px; height: 28px; border-radius: 50%; background: var(--white); display: flex; align-items: center; justify-content: center; }
  .contact__badge svg { width: 17px; height: 17px; }
  .contact--phone { top: 403px; font-size: 29px; }
  .contact--mail { top: 444px; font-size: 20px; }
  .contact--web { top: 480px; font-size: 20px; }

  .stamp { position: absolute; left: 661px; top: 45px; width: 105px; height: 124px; background: var(--blue-pale); }
  .address-line { position: absolute; left: 432px; width: 334px; height: 1px; background: var(--rule); }
</style>
</head>
<body>

<section class="card card--front">
  <div class="brand"><span class="brand__mark"></span>Fernvale Accounting</div>

  <div class="service-col service-col--books"></div>
  <div class="service-col service-col--reports"></div>
  <div class="service-col service-col--payroll"></div>

  <h1 class="services-title"><span class="our">OUR</span><span class="rest">SERVICES</span></h1>

  <article class="service service--books">
    <svg class="service__icon" viewBox="0 0 84 84" fill="none" stroke="#fff" stroke-width="3.5">
      <circle cx="42" cy="42" r="38"/>
      <circle cx="42" cy="42" r="29"/>
      <path d="M50 31c-2-4-14-5-15 2-1 7 16 4 15 12-1 7-13 6-16 1M42 24v36" stroke-linecap="round"/>
    </svg>
    <h2 class="service__name">BOOKKEEPING</h2>
    <p class="service__text">We offer LedgerCloud Online<br>setup &amp; ongoing bookkeep-<br>ing, including daily journal<br>entries, accounts payables &amp;<br>receivables, bill pay, sales<br>tax reporting &amp; payments,<br>account reconciliation, &amp;<br>more.</p>
  </article>

  <article class="service service--reports">
    <svg class="service__icon" viewBox="0 0 84 84" fill="none" stroke="#fff" stroke-width="2.5">
      <rect x="14" y="2" width="64" height="80" rx="3"/>
      <circle cx="29" cy="19" r="8"/><circle cx="29" cy="19" r="3.5"/>
      <path d="M52 22l6-5 6 7 8-2M53 18v-5h4" stroke-linecap="round"/>
      <path d="M25 41v10M22 44c0-3 7-3 7 0s-7 2-7 5 7 3 7 0" />
      <rect x="47" y="36" width="5" height="15"/><rect x="56" y="42" width="5" height="9"/><rect x="65" y="39" width="5" height="12"/>
      <path d="M22 60h48M22 66h48M22 72h48"/>
    </svg>
    <h2 class="service__name">FINANCIAL REPORTING</h2>
    <p class="service__text">We'll provide easy to under-<br>stand financial reports that<br>allow you and your team to<br>manage cash flow, create bud-<br>gets and make forecasting deci-<br>sions.</p>
  </article>

  <article class="service service--payroll">
    <svg class="service__icon" viewBox="0 0 90 84" fill="none" stroke="#fff" stroke-width="3">
      <circle cx="14" cy="11" r="8"/><circle cx="45" cy="11" r="8"/><circle cx="76" cy="11" r="8"/>
      <path d="M2 48V33c0-8 5-12 12-12s12 4 12 12v7M64 40v-7c0-8 5-12 12-12s12 4 12 12v15M33 40v-7c0-8 5-12 12-12s12 4 12 12v7"/>
      <path d="M2 48h30M58 48h30M8 48v32M28 48v32M62 48v32M82 48v32M22 40h46v10H22zM45 50v30M36 80h18"/>
    </svg>
    <h2 class="service__name">PAYROLL PROCESSING</h2>
    <p class="service__text">Whether you have 5 employ-<br>ees or 100+, payroll can be<br>an overwhelming and time<br>consuming task.&nbsp; We offer<br>full service payroll process-<br>ing, including employee on<br>boarding and reporting.</p>
  </article>
</section>

<section class="card card--back">
  <div class="promo">
    <p class="promo__lead">Specializing in Cloud-Based<br>Bookkeeping &amp; Payroll Process-<br>ing with LedgerCloud Online .</p>
    <div class="price">
      <p class="price__lead">Prices starting at</p>
      <p class="price__amount">$750/mo</p>
    </div>
    <p class="cta">BOOK A
      <svg class="cta__icon" viewBox="0 0 24 24" fill="#fff" aria-label="call"><path d="M6.6 2.2c.6-.4 1.4-.3 1.8.3l2.2 3.3c.4.6.3 1.4-.2 1.9L9 9c.9 2.3 3.6 5 5.9 5.9l1.3-1.4c.5-.5 1.3-.6 1.9-.2l3.3 2.2c.6.4.7 1.2.3 1.8l-1.3 2.1c-.7 1.1-2.1 1.6-3.4 1.2C10.4 19 5 13.6 3.4 7c-.4-1.3.1-2.7 1.2-3.4z"/></svg>
      TODAY</p>
    <p class="contact contact--phone"><span class="contact__badge"><svg viewBox="0 0 24 24" fill="#1a5daa"><path d="M6.6 2.2c.6-.4 1.4-.3 1.8.3l2.2 3.3c.4.6.3 1.4-.2 1.9L9 9c.9 2.3 3.6 5 5.9 5.9l1.3-1.4c.5-.5 1.3-.6 1.9-.2l3.3 2.2c.6.4.7 1.2.3 1.8l-1.3 2.1c-.7 1.1-2.1 1.6-3.4 1.2C10.4 19 5 13.6 3.4 7c-.4-1.3.1-2.7 1.2-3.4z"/></svg></span>1.800.555.0142</p>
    <p class="contact contact--mail"><span class="contact__badge"><svg viewBox="0 0 24 24" fill="none" stroke="#1a5daa" stroke-width="2"><rect x="3" y="6" width="18" height="12"/><path d="M3 6l9 7 9-7M3 18l7-6M21 18l-7-6"/></svg></span>info@fernvaleaccounting.com</p>
    <p class="contact contact--web"><span class="contact__badge"><svg viewBox="0 0 24 24" fill="none" stroke="#1a5daa" stroke-width="1.8"><circle cx="12" cy="12" r="9"/><ellipse cx="12" cy="12" rx="4" ry="9"/><path d="M3 12h18M5 7h14M5 17h14"/></svg></span>www.fernvaleaccounting.com</p>
  </div>

  <div class="stamp"></div>
  <div class="address-line" style="top:231px"></div>
  <div class="address-line" style="top:277px"></div>
  <div class="address-line" style="top:322px"></div>
  <div class="address-line" style="top:374px"></div>
</section>

</body>
</html>
```